design a high conversion homepage for datingsite

For my datingsite i want a new homepage ( must have same funcions as now) and must keep fitting to the rest of the website.

What i want is that the conversions of visitors to go to members as high as possible. So do you know a way to make a homepage where most visitors will sign up... then add youre design.

( if you want there can be pictures on homepage of profiles)

Please check file for the url

```html
<!DOCTYPE html>
<html lang="en">
<head>
<meta charset="utf-8">
<title>Velmira – Road To Love</title>
<link href="https://fonts.googleapis.com/css2?family=Arimo:wght@400;700&family=Open+Sans:wght@400;600;700&display=swap" rel="stylesheet">
<style>
:root{
  --crimson:#a8243f;
  --crimson-deep:#7a1129;
  --maroon:#5e0c1f;
  --maroon-dark:#4a0717;
  --pink:#f58aa6;
  --red:#d4001a;
  --red-text:#d2141e;
  --beige:#fbebd0;
  --brown:#8a5a3c;
  --body-text:#a6737c;
  --white:#ffffff;
}
*{box-sizing:border-box;margin:0;padding:0}
html,body{width:1200px;height:1200px;overflow:hidden}
body{
  position:relative;
  font-family:'Open Sans',Arial,sans-serif;
  background:radial-gradient(ellipse at 50% 18%,#c23553 0%,var(--crimson) 40%,var(--crimson-deep) 100%);
}
.abs{position:absolute}
/* login bar */
.login-bar{left:507px;top:0;width:633px;height:73px;background:var(--maroon);border-radius:0 0 10px 10px;color:var(--white);font-size:14px}
.login-bar label{position:absolute;top:16px}
.login-bar .field{position:absolute;top:14px;width:160px;height:24px;background:var(--white);border:1px solid #ccc}
.btn{display:inline-block;background:linear-gradient(#e2172c,#b10012);color:var(--white);border-radius:5px;font-weight:600;text-align:center}
.login-bar .btn{position:absolute;left:533px;top:13px;width:69px;height:25px;line-height:25px;font-size:14px}
.login-bar .links{position:absolute;left:20px;top:52px;font-size:13px;color:#e0c9ce}
.login-bar .links a{color:#e0507a;text-decoration:underline}
/* hero */
.hero-photo{left:87px;top:0;width:406px;height:447px;background:linear-gradient(160deg,#6b3a2c 0%,#c98c78 45%,#e9b8a8 60%,#a03048 100%);border-radius:0 0 6px 6px}
.brand{left:504px;top:180px;font-family:'Arimo',Arial,sans-serif;font-weight:700;font-size:66px;color:var(--pink);letter-spacing:1px}
.tagline{left:604px;top:247px;font-family:'Arimo',Arial,sans-serif;font-weight:700;font-size:21px;color:var(--white)}
/* quick links */
.quick{left:804px;top:83px;width:340px;height:293px;background:linear-gradient(#c0466a,#a8304f);border:3px solid #d0637f;border-radius:12px;color:var(--white);font-size:14px}
.quick h2{position:absolute;left:25px;top:10px;font-size:21px;font-weight:700}
.quick .rule{position:absolute;left:25px;top:40px;width:292px;border-top:2px dotted #f1b2c2}
.quick .row{position:absolute;left:22px}
.quick .in{position:absolute;height:24px;background:var(--maroon-dark);border-radius:4px;font-size:12px;color:#c98894;padding:3px 6px}
.quick .btn{position:absolute;left:130px;top:246px;width:168px;height:32px;line-height:32px;font-size:14px;font-weight:400;border-radius:3px}
/* nav */
.nav{left:53px;top:387px;width:1091px;height:56px;background:linear-gradient(#6e1026,var(--maroon-dark));border-radius:8px;display:flex;align-items:center;padding-left:28px;gap:40px}
.nav a{color:var(--white);font-size:18px;text-decoration:none;display:flex;align-items:center;gap:8px}
/* main */
.main{left:53px;top:453px;width:1091px;height:718px;background:var(--white);border-radius:8px}
.steps{left:67px;top:464px;width:340px;height:283px;background:var(--beige);border-radius:12px}
.steps h2{position:absolute;left:22px;top:4px;color:var(--red-text);font-size:25px;font-weight:700}
.steps h3{position:absolute;left:20px;top:40px;color:var(--brown);font-size:20px;font-weight:700}
.steps .btn{position:absolute;left:217px;top:249px;width:100px;height:28px;line-height:28px;font-size:14px}
.para{color:var(--body-text);font-size:13.4px;line-height:19.6px;text-align:justify}
.welcome h1{font-family:'Arimo',Arial,sans-serif;font-size:28px;color:var(--maroon);font-weight:700}
.welcome h1 span{font-size:20px;color:#b01e3c}
.read{position:absolute;height:28px;line-height:28px;font-size:14px;width:100px}
.latest{left:908px;top:464px;width:220px;height:689px;background:var(--beige);border-radius:12px}
.latest h2{text-align:center;margin-top:13px;color:var(--brown);font-size:21px;font-weight:700}
.profile{position:absolute;left:15px;width:194px}
.profile .ph{height:104px;border-radius:12px;border:3px solid var(--white)}
.profile .cap{margin-top:14px;font-size:15px;padding-left:15px}
.profile .name{color:var(--brown);text-decoration:underline}
.profile .det{color:var(--red-text);text-decoration:underline;font-size:14px;margin-left:10px}
.story h2{font-size:20px;font-weight:700;color:#111}
.story .ph{position:absolute;top:47px;width:173px;height:123px;border-radius:10px;border:3px solid #eee}
.story .who{position:absolute;left:191px;top:41px;color:var(--red-text);font-weight:700;text-decoration:underline;font-size:15px}
.story .para{position:absolute;left:191px;top:69px;width:206px}
.story .more{position:absolute;right:4px;top:157px;color:var(--red-text);font-size:13.4px;text-decoration:underline}
.more-link{color:var(--red-text);font-size:13.4px;text-decoration:underline}
.chance h2{color:var(--red-text);font-size:16px;font-weight:700;margin-bottom:4px}
.footer{left:0;top:1178px;width:1200px;text-align:center;color:#e3728f;font-size:13.4px}
</style>
</head>
<body>
<div class="abs hero-photo" role="img" aria-label="Smiling young couple embracing"></div>

<div class="abs login-bar">
  <label style="left:20px">Username :</label><span class="field" style="left:104px"></span>
  <label style="left:288px">Password:</label><span class="field" style="left:366px"></span>
  <span class="btn">Login</span>
  <div class="links"><a>Passport Reminder</a> No Account Yet? <a>Create One</a></div>
</div>

<div class="abs brand">Velmira</div>
<div class="abs tagline">Road To Love</div>

<div class="abs quick">
  <h2>Quick Links</h2><div class="rule"></div>
  <span class="row" style="top:52px">First Name :</span><span class="in" style="left:128px;top:49px;width:188px"></span>
  <span class="row" style="top:86px">I am a :</span><span class="in" style="left:89px;top:83px;width:84px">Woman ▾</span>
  <span class="row" style="left:188px;top:86px">Seeking :</span><span class="in" style="left:260px;top:83px;width:72px">Men ▾</span>
  <span class="row" style="top:119px">Country :</span><span class="in" style="left:128px;top:116px;width:188px">a date</span>
  <span class="row" style="top:153px">Email :</span><span class="in" style="left:128px;top:150px;width:188px"></span>
  <span class="row" style="top:186px">Confirm Email :</span><span class="in" style="left:128px;top:183px;width:188px"></span>
  <span class="row" style="top:220px">Password :</span><span class="in" style="left:128px;top:217px;width:188px"></span>
  <span class="btn">Sign Me Up For Free</span>
</div>

<nav class="abs nav">
  <a><svg width="18" height="16" viewBox="0 0 18 16"><path d="M9 15 1 7a4 4 0 0 1 8-4 4 4 0 0 1 8 4z" fill="#d4001a"/></svg>Home</a>
  <a><svg width="18" height="16" viewBox="0 0 18 16"><path d="M9 15 1 7a4 4 0 0 1 8-4 4 4 0 0 1 8 4z" fill="#d4001a"/></svg>My Profile</a>
  <a><svg width="18" height="16" viewBox="0 0 18 16"><path d="M9 15 1 7a4 4 0 0 1 8-4 4 4 0 0 1 8 4z" fill="#d4001a"/></svg>My Soulmate</a>
</nav>

<div class="abs main"></div>

<section class="abs steps">
  <h2>Dont Stay Alone</h2>
  <h3>Three Steps To Success</h3>
  <span class="btn">Click Here</span>
</section>

<section class="abs welcome" style="left:428px;top:472px;width:459px;height:280px">
  <h1>Welcome <span>To Velmira</span></h1>
  <p class="para" style="margin-top:4px">All our lives, we've always wanted to find someone to love. Someone who will love us in return and accept us for all that we are and we are not. Because once we find that someone, magic begins. The days are brighter and our lives merrier. We smile sweeter and we feel lighter. Some of us find love easily while some of us, with difficulty. Some have been heartbroken and others have given hope. That's what we are here for: To help you find that someone who will be able to bring magic into your life. Take our hand, and we will lead you to a journey of discovery. Go on, take a chance with us. Take a chance with love. And let the magic begin...</p>
  <span class="btn read" style="left:353px;top:246px">Read More</span>
</section>

<section class="abs story" style="left:64px;top:770px;width:400px;height:180px">
  <h2 style="margin-left:7px">Sucessful Story</h2>
  <div class="ph" style="left:0;background:linear-gradient(120deg,#8a6a5a,#d9b8a2,#5c6e8c)" role="img" aria-label="Happy couple by the sea"></div>
  <a class="who">Lena &amp; Tom</a>
  <p class="para">Donec varius congue ipsum non condimentum. Mauris tempus feugiat nibh, a vestibulum dolor vehicula eu. Curabitur sed</p>
  <a class="more">Read More</a>
</section>

<section class="abs story" style="left:480px;top:770px;width:406px;height:180px">
  <h2>Sucessful Story</h2>
  <div class="ph" style="left:0;background:linear-gradient(120deg,#3e3a36,#d8b48e,#6a5644)" role="img" aria-label="Smiling couple posing together"></div>
  <a class="who" style="left:191px">Lena &amp; Tom</a>
  <p class="para" style="left:191px">Donec varius congue ipsum non condimentum. Mauris tempus feugiat nibh, a vestibulum dolor vehicula eu. Curabitur sed</p>
  <a class="more">Read More</a>
</section>

<section class="abs chance" style="left:68px;top:981px;width:822px">
  <h2>Take a Chance at Love With us at V.</h2>
  <p class="para">All our lives, we've always wanted to find someone to love. Someone who will love us in return and accept us for all that we are and we are not. Because once we find that someone, magic begins. The days are brighter and our lives merrier. We smile sweeter and we feel lighter. Some of us find love easily while some of us, with difficulty. Some have been heartbroken and others have given hope. That's what we are here for: To help you find that someone who will be able to bring magic into your life. Take our hand, and we will lead you to a journey of discovery. Go on, take a chance with us. Take a chance with love. And let the magic begin...</p>
  <p style="text-align:right;margin-top:8px"><a class="more-link">Read More</a></p>
</section>

<aside class="abs latest">
  <h2>Latest Added</h2>
  <div class="profile" style="top:57px"><div class="ph" style="background:linear-gradient(135deg,#f4eeee,#9a6a55,#f0e8e8)" role="img" aria-label="Member profile photo"></div><div class="cap"><a class="name">Mira Dolens</a><a class="det">Details</a></div></div>
  <div class="profile" style="top:211px"><div class="ph" style="background:linear-gradient(135deg,#111,#6a4a3c,#e8e0dc,#111)" role="img" aria-label="Member profile photo"></div><div class="cap"><a class="name">Mira Dolens</a><a class="det">Details</a></div></div>
  <div class="profile" style="top:366px"><div class="ph" style="background:linear-gradient(135deg,#5c6670,#8a6a58,#3a8ad0)" role="img" aria-label="Member profile photo"></div><div class="cap"><a class="name">Mira Dolens</a><a class="det">Details</a></div></div>
  <div class="profile" style="top:525px"><div class="ph" style="background:linear-gradient(135deg,#f0f0f0,#2a1e1a,#c8a290,#f0f0f0)" role="img" aria-label="Member profile photo"></div><div class="cap"><a class="name">Mira Dolens</a><a class="det">Details</a></div></div>
</aside>

<footer class="abs footer">Copyright©2011.All Right Reserverd.Velmira Dating Website</footer>
</body>
</html>
```